Renewal of the Ferolanza SA Website

Ferolanza SA is a metal construction company active in industrial piping, boilermaking and metal framing. We would like to renew our site.

This website must be ready to work with Wordpress.

The site will contain the following pages: Home, skills, presentation, contact.

The site must reflect the field of the metal construction sector. It must be clear and easily understandable. The objective is not to win mandates with but to present the company and its capabilities.

I have inserted the pages of our old presentations, to describe our sector but we do not want to reuse these elements, we are waiting for your creativity to surprise us. In the 2nd phase we will complete with new images if necessary and texts

Target Market(s)

International companies in the food, chemical and pharmaceutical sectors

Industry/Entity Type

Alimentaire, pharma, chimie

Number of Pages Required

4 page

Font styles to use
Sans Serif

Colors
0054AA
0677BA
7BADD7
CADEEF
E8F1F8

Requirements
Must have
• It must contain at least the requested pages, images of illustrations, places for descriptions
Should not have
• Elements that appear or disappear, too flash,

```html
<!DOCTYPE html>
<html lang="en">
<head>
<meta charset="utf-8">
<title>Ferolanza SA – Metal Construction</title>
<link href="https://fonts.googleapis.com/css2?family=Poppins:ital,wght@0,300;0,400;0,500;0,600;0,700;0,800;1,300;1,700;1,800&family=Hind:wght@400;500&display=swap" rel="stylesheet">
<style>
:root{
  --navy:#1a3a8f;
  --blue:#0c3b95;
  --blue-bright:#1f4fb5;
  --ink:#222;
  --muted:#8a8a8a;
  --pill:#3b3b3b;
  --line:#d9d9d9;
  --sky:#4fa3e8;
  --cyan:#38c8ea;
  --orange:#ff6a3d;
  --footer:#13213b;
  --bar:#1f3f92;
  --skills-bg:#efeff1;
}
*{margin:0;padding:0;box-sizing:border-box}
html,body{width:1200px;height:2584px;overflow:hidden;background:#fff}
body{position:relative;font-family:"Poppins",sans-serif;color:var(--ink)}
.abs{position:absolute}
.pill{position:absolute;display:flex;align-items:center;justify-content:center;border-radius:20px;color:#fff;font-family:"Poppins",sans-serif;font-weight:500}
.pill.dark{background:var(--pill)}
.pill.blue{background:var(--blue)}
.brand{position:absolute;display:flex;align-items:center;gap:10px;font-family:"Poppins",sans-serif;font-weight:800;letter-spacing:1px}
.brand .dot{width:34px;height:34px;border-radius:50%;background:var(--navy)}
/* header */
.site-header{position:absolute;left:0;top:0;width:1200px;height:82px;background:#fff}
.nav a{position:absolute;top:33px;font-size:12px;color:#222;text-decoration:none}
.nav a.active{color:var(--blue-bright);border-bottom:1px solid var(--blue-bright)}
.social span{position:absolute;border-radius:50%}
/* hero */
.hero-copy{position:absolute;left:628px;top:220px;color:#fff}
.hero-kicker{font-weight:300;font-style:italic;font-size:17px}
.hero-title{font-weight:800;font-style:italic;font-size:32px;line-height:36px;margin-top:4px;letter-spacing:.3px}
.hero-sub{font-weight:300;font-style:italic;font-size:20px;line-height:23px;margin-top:12px;width:360px}
.hero-sub b{font-weight:800}
.hl-orange{color:var(--orange)}.hl-sky{color:var(--sky)}.hl-cyan{color:var(--cyan)}
/* about */
.about h2{position:absolute;left:200px;top:712px;font-size:30px;font-weight:700;color:var(--navy)}
.about p{position:absolute;left:200px;width:345px;font-family:"Hind",sans-serif;font-size:12.5px;line-height:17.5px;color:#222}
.badge{position:absolute;left:603px;top:829px;width:112px;height:98px;background:var(--blue);border:4px solid #fff;border-radius:6px;color:#fff;text-align:center;box-shadow:0 2px 6px rgba(0,0,0,.15)}
.badge strong{display:block;font-size:28px;font-weight:700;line-height:30px;margin-top:12px}
.badge em{display:block;font-style:normal;font-weight:700;font-size:13px;line-height:15px}
.badge small{display:block;font-weight:500;font-size:10px;letter-spacing:.5px}
/* skills */
.section-title{position:absolute;width:1200px;text-align:center;font-weight:700;color:var(--navy)}
.skill-card{position:absolute;top:1201px;width:204px;height:213px;background:#fff;border:1px solid #cfcfcf;border-radius:6px;padding:4px}
.skill-card div{width:100%;height:100%;border-radius:3px}
.skill-label{position:absolute;top:1421px;width:204px;text-align:center;font-size:13px;font-weight:500;color:#444}
/* clients */
.client{position:absolute;top:1713px;width:200px;text-align:center}
.client .ring{width:106px;height:106px;margin:0 auto;border-radius:50%;border:2px solid #c9c9cf;display:flex;align-items:center;justify-content:center;background:#fff;box-shadow:0 3px 6px rgba(0,0,0,.08)}
.client .ring.on{background:var(--blue);border-color:#9db0d6}
.client h3{margin-top:8px;font-size:13.5px;font-weight:600;color:var(--navy);line-height:16px}
.client p{margin-top:4px;font-size:11px;line-height:15px;color:var(--muted)}
/* contact card */
.contact-card{position:absolute;left:250px;top:1984px;width:697px;height:314px;background:#fff;border-radius:14px;box-shadow:0 4px 16px rgba(0,0,0,.12)}
.contact-card h2{position:absolute;left:427px;top:26px;font-size:19px;font-weight:600;color:var(--navy)}
.field{position:absolute;left:428px;width:233px;height:30px;border:1px solid #dedede;border-radius:3px;display:flex;align-items:center;gap:7px;padding-left:7px;font-size:10px;color:#999}
.field svg{flex:none}
/* footer */
.footer h4{position:absolute;font-size:16px;font-weight:600;color:#3f6fe0}
.footer .info{position:absolute;left:444px;display:flex;gap:8px;color:#fff;font-size:12px;line-height:16px}
.footer .links a{position:absolute;left:665px;font-size:12px;color:#fff;text-decoration:none}
.footer .links a.active{color:#4d7de8;border-bottom:1px solid #4d7de8}
.bottom-bar{position:absolute;left:0;top:2545px;width:1200px;height:39px;background:var(--bar);color:#fff;font-size:12px}
</style>
</head>
<body>

<header class="site-header">
  <div class="brand" style="left:150px;top:22px;font-size:24px;color:var(--navy)"><span class="dot"></span>FEROLANZA SA</div>
  <nav class="nav">
    <a class="active" style="left:538px" href="#">Home</a>
    <a style="left:594px" href="#">About Us</a>
    <a style="left:667px" href="#">Skills</a>
    <a style="left:716px" href="#">Contact Us</a>
  </nav>
  <div class="social" aria-label="Social links">
    <span style="left:817px;top:37px;width:8px;height:8px;border:1px solid #777"></span>
    <span style="left:839px;top:29px;width:24px;height:24px;background:var(--blue)"></span>
    <span style="left:876px;top:37px;width:8px;height:8px;border:1px solid #777"></span>
  </div>
  <div class="pill dark" style="left:920px;top:24px;width:126px;height:33px;font-size:12.5px;font-weight:400">Quick Inquiry</div>
</header>

<section class="hero">
  <svg class="abs" style="left:0;top:82px" width="1200" height="530" viewBox="0 82 1200 530" aria-hidden="true">
    <defs>
      <linearGradient id="heroFill" x1="0" y1="0" x2="1" y2="0">
        <stop offset="0" stop-color="#2a4a66"/>
        <stop offset=".45" stop-color="#1d3347"/>
        <stop offset="1" stop-color="#141b24"/>
      </linearGradient>
    </defs>
    <path d="M0 82H1200V475Q600 690 0 475Z" fill="url(#heroFill)" role="img" aria-label="Industrial plant interior with large steel pipework and valves"/>
    <path d="M85 505Q600 690 1115 505Q600 665 85 505Z" fill="#1d3f9a"/>
  </svg>
  <div class="hero-copy">
    <div class="hero-kicker">FEROLANZA SA IS A</div>
    <div class="hero-title">METAL CONSTRUCTION<br>COMPANY</div>
    <div class="hero-sub">active in <b class="hl-orange">INDUSTRIAL PIPING</b>, <b class="hl-sky">BOILER MAKING</b> &amp; <b class="hl-cyan">METAL FRAMING</b>.</div>
  </div>
  <div class="pill blue" style="left:629px;top:386px;width:113px;height:34px;font-size:12px">Contact Us</div>
</section>

<section class="about">
  <h2>About Us</h2>
  <p style="top:763px">Fondée en 1996, FEROLANZA SA, est une entreprise spécialisée dans l'étude, la conception, le montage et l'installation de tuyauterie industrielle.</p>
  <p style="top:833px">De l'étude d'un projet et jusqu'à la résolution de problèmes de maintenance dans vos installations, nous vous proposons des solutions rapides et adaptées à vos exigences, quel que soit votre secteur d'activité.</p>
  <div class="pill dark" style="left:200px;top:922px;width:107px;height:29px;font-size:11.5px;font-weight:400">Read More</div>
  <div class="abs" style="left:832px;top:733px;width:165px;height:267px;border:3px solid #dbe3f1;border-radius:10px"></div>
  <div class="abs" role="img" aria-label="Engineer and technician in hard hats reviewing work in a factory hall" style="left:647px;top:682px;width:338px;height:306px;border-radius:10px;background:linear-gradient(160deg,#5c7393,#2c3d58 60%,#47526a)"></div>
  <div class="badge"><strong>20+</strong><em>YEARS OF</em><small>EXPERIENCE</small></div>
</section>

<section class="skills">
  <svg class="abs" style="left:0;top:1055px" width="1200" height="540" viewBox="0 1055 1200 540" aria-hidden="true">
    <path d="M0 1140Q600 990 1200 1140V1515Q600 1660 0 1515Z" fill="var(--skills-bg)"/>
    <path d="M90 1131Q600 1000 1110 1131Q600 1025 90 1131Z" fill="#1d3f9a"/>
    <path d="M90 1520Q600 1650 1110 1520Q600 1625 90 1520Z" fill="#1d3f9a"/>
  </svg>
  <h2 class="section-title" style="top:1137px;font-size:30px">Skills</h2>
  <div class="skill-card" style="left:150px"><div role="img" aria-label="Designer working on a mechanical part on screen" style="background:linear-gradient(150deg,#33446a,#9aa0ad)"></div></div>
  <div class="skill-card" style="left:381px"><div role="img" aria-label="Quality and compliance concept with glowing icons" style="background:radial-gradient(circle,#2b79c9,#0e1f3c 70%)"></div></div>
  <div class="skill-card" style="left:612px"><div role="img" aria-label="Relaxed employee at a laptop in an office" style="background:linear-gradient(160deg,#6f5d45,#c9c4ba)"></div></div>
  <div class="skill-card" style="left:842px"><div role="img" aria-label="Speedometer dial at high speed" style="background:radial-gradient(circle at 50% 60%,#c0562a,#1a2436 70%)"></div></div>
  <div class="skill-label" style="left:150px">Étude Et Conception</div>
  <div class="skill-label" style="left:381px">Qualité Et Conformité</div>
  <div class="skill-label" style="left:612px">Flexibilité Et Disponibilité</div>
  <div class="skill-label" style="left:842px">Rapidité Et Efficacité</div>
  <div class="pill dark" style="left:535px;top:1477px;width:125px;height:29px;font-size:12px;font-weight:400">Quick Inquiry</div>
</section>

<section class="clients">
  <h2 class="section-title" style="top:1640px;font-size:33px">Clients We Serve</h2>
  <div class="client" style="left:181px">
    <div class="ring"><svg width="44" height="44" viewBox="0 0 44 44" fill="none" stroke="#1f3f92" stroke-width="2"><rect x="6" y="8" width="10" height="30"/><rect x="20" y="16" width="18" height="22"/></svg></div>
    <h3>Charpentes Et<br>Chaudronnerie</h3>
    <p>Lorem Ipsum is simply dummy<br>text of the printing industry.</p>
  </div>
  <div class="client" style="left:392px">
    <div class="ring"><svg width="44" height="44" viewBox="0 0 44 44" fill="none" stroke="#1f3f92" stroke-width="2"><path d="M16 6h12M19 6v12L9 38h26L25 18V6"/></svg></div>
    <h3>Chemical Industrie</h3>
    <p>Lorem Ipsum is simply dummy<br>text of the printing industry.</p>
  </div>
  <div class="client" style="left:603px">
    <div class="ring on"><svg width="44" height="44" viewBox="0 0 44 44" fill="none" stroke="#fff" stroke-width="2"><path d="M6 8h32M12 8v8M32 8v8"/><rect x="6" y="30" width="32" height="8" rx="4"/><circle cx="16" cy="24" r="3"/><circle cx="28" cy="24" r="3"/></svg></div>
    <h3>Food Industrie</h3>
    <p>Lorem Ipsum is simply dummy<br>text of the printing industry.</p>
  </div>
  <div class="client" style="left:814px">
    <div class="ring"><svg width="44" height="44" viewBox="0 0 44 44" fill="none" stroke="#1f3f92" stroke-width="2"><path d="M13 18a9 9 0 0 1 18 0z"/><circle cx="22" cy="23" r="5"/><path d="M10 38v-4a8 8 0 0 1 8-8h8a8 8 0 0 1 8 8v4z"/></svg></div>
    <h3>Chaudronnerie</h3>
    <p>Lorem Ipsum is simply dummy<br>text of the printing industry.</p>
  </div>
  <div class="pill blue" style="left:656px;top:1882px;width:94px;height:25px;font-size:10.5px;font-weight:400">Read More</div>
</section>

<footer class="footer">
  <svg class="abs" style="left:0;top:2230px" width="1200" height="316" viewBox="0 2230 1200 316" aria-hidden="true">
    <path d="M0 2345Q600 2175 1200 2345V2545H0Z" fill="var(--footer)" role="img" aria-label="Dark industrial backdrop"/>
    <path d="M90 2322Q600 2190 1110 2322Q600 2215 90 2322Z" fill="#1d3f9a"/>
  </svg>
  <div class="brand" style="left:165px;top:2408px;font-size:22px;color:#c9d3e6"><span class="dot" style="background:#c9d3e6"></span>FEROLANZA SA</div>
  <h4 style="left:444px;top:2359px">Conatct Info</h4>
  <div class="info" style="top:2395px"><svg width="13" height="16" viewBox="0 0 12 16"><path d="M6 0a6 6 0 0 0-6 6c0 4.5 6 10 6 10s6-5.5 6-10a6 6 0 0 0-6-6zm0 8.5A2.5 2.5 0 1 1 6 3.5a2.5 2.5 0 0 1 0 5z" fill="#3f6fe0"/></svg><span>Rue des Forges 12 / CP 7<br>1900 Valmont 2</span></div>
  <div class="info" style="top:2441px"><svg width="13" height="14" viewBox="0 0 14 14"><path d="M3 0l2.5 3-1.5 2a8 8 0 0 0 5 5l2-1.5L14 11l-2 3C5 14 0 9 0 2z" fill="#3f6fe0"/></svg><span>+41 (0) 21/555 01 42</span></div>
  <div class="info" style="top:2470px"><svg width="13" height="14" viewBox="0 0 14 10"><rect width="14" height="10" fill="#3f6fe0"/><path d="M0 0l7 5 7-5" stroke="#fff" fill="none"/></svg><span>info@ferolanza-sa.example</span></div>
  <h4 style="left:665px;top:2358px">Quick Link</h4>
  <div class="links">
    <a class="active" style="top:2389px" href="#">Home</a>
    <a style="top:2414px" href="#">About Us</a>
    <a style="top:2438px" href="#">Skills</a>
    <a style="top:2463px" href="#">Contact Us</a>
  </div>
  <div class="abs" role="img" aria-label="Location map of the company premises" style="left:815px;top:2362px;width:232px;height:120px;background:linear-gradient(135deg,#e9ebee,#d7dde4)"></div>
  <div class="bottom-bar">
    <span class="abs" style="left:150px;top:12px">© 2023 Ferolanza SA. all right reserved</span>
    <span class="abs" style="left:966px;top:16px;width:7px;height:7px;border-radius:50%;background:#fff"></span>
    <span class="abs" style="left:995px;top:16px;width:7px;height:7px;border-radius:50%;background:#fff"></span>
    <span class="abs" style="left:1025px;top:16px;width:7px;height:7px;border-radius:50%;background:#fff"></span>
  </div>
</footer>

<section class="contact-card">
  <div class="abs" role="img" aria-label="Smiling workers in hard hats and overalls in a factory" style="left:6px;top:6px;width:383px;height:302px;border-radius:8px 0 0 8px;background:linear-gradient(120deg,#3a5a86,#1f3352 55%,#5a6f8f)"></div>
  <h2>Let’s Work Together!</h2>
  <div class="field" style="top:63px"><svg width="11" height="11" viewBox="0 0 12 12" fill="none" stroke="#1f3f92" stroke-width="1.3"><circle cx="6" cy="4" r="3"/><path d="M1 12a5 5 0 0 1 10 0"/></svg>Name</div>
  <div class="field" style="top:102px"><svg width="11" height="9" viewBox="0 0 12 9" fill="none" stroke="#1f3f92" stroke-width="1.3"><rect x=".5" y=".5" width="11" height="8"/><path d="M.5 .5l5.5 4 5.5-4"/></svg>Email</div>
  <div class="field" style="top:142px"><svg width="8" height="12" viewBox="0 0 8 12" fill="none" stroke="#1f3f92" stroke-width="1.3"><rect x=".6" y=".6" width="6.8" height="10.8" rx="1"/></svg>Phone</div>
  <div class="field" style="top:181px;height:60px;align-items:flex-start;padding-top:9px"><svg width="11" height="11" viewBox="0 0 12 12" fill="none" stroke="#1f3f92" stroke-width="1.3"><path d="M1 1h10v7L8 11H1z"/></svg>Message</div>
  <div class="pill dark" style="left:428px;top:259px;width:97px;height:29px;font-size:12px">Submit</div>
</section>

</body>
</html>
```